Business Card: RW Office Partners - Your tidy answer finder

Business Name: RW Office Partners
Website: www.rwofficepartners.com.au
Email: marisol@rwofficepartners.com.au
Mobile: 61 487 902 346
Facebook: @rwofficepartners
Instrgram: @rwofficepartners

Brading Colours:
HEX
#986474
#ddccd3
#7a8498
#c9d8e4
#000000
#ffffff

Tag Line: Your organised problem solver

Link to DRAFT website:
https://helpdeskhub.sitebuilderx.com/rw-office-partners

About Page from the website:
My name is Marisol Bramwell, and I would love to assist you to become more productive in your day to day and achieve your business and personal goals.
My mission is to give you time, time to work on the important tasks of your business or to be able to spend more time with your family. I will take on the tasks you don’t have time for, don’t know well or simply don’t like to do.
I have an extensive background in Administration, Tender Coordination, Document Control, WHS and Quality Management working primarily in the Construction, Mining and Corporate World.
I am passionate about being organised, having order and making things in your life (and mine) easier! I love to watch something unfold and grow into something amazing! I am known for being the go-to problem solver, the organiser of all things, producing high standards of work even under pressure. I’m also a confident communicator, and I understand that you’re busy running your business.

Target Market(s)

Small to Medium Business who require assistance in their business by a virtual assistant.

Industry/Entity Type

Virtual Assistant

Contact Information for Business Card

Mobile: 61 487 902 346

Font styles to use
Sans Serif

Colors
ffffff

Requirements
Must have
• Branding Colours as outlined.
Contact Details as outlined.
Logo as provided.
Proper contact details - mobile, facebook, instragm, website.
Simple, Elegant, very clean looking.
Should not have
• Note cute with pictures.
Not too girly as still want to market to construction companies.

```html
<!DOCTYPE html>
<html lang="en">
<head>
<meta charset="utf-8">
<title>RW Office Partners – Business Card</title>
<link rel="stylesheet" href="https://fonts.googleapis.com/css2?family=Arimo:wght@400;500&display=swap">
<style>
  :root {
    --mauve: #986474;
    --mauve-light: #ddccd3;
    --slate: #7a8498;
    --mist: #c9d8e4;
    --black: #000000;
    --card-dark: #111111;
    --white: #ffffff;
    --ink: #1e1e1e;
    --backdrop: #dcdcdc;
  }
  * { box-sizing: border-box; margin: 0; padding: 0; }
  html, body { width: 1200px; height: 802px; overflow: hidden; }
  body {
    background: var(--backdrop);
    font-family: "Arimo", Arial, sans-serif;
    position: relative;
  }
  .card {
    position: absolute;
    top: 239px;
    width: 540px;
    height: 324px;
    overflow: hidden;
  }
  .card--front { left: 40px; background: var(--white); }
  .card--back { left: 620px; background: var(--card-dark); }

  .accent-band {
    position: absolute;
    left: 0; top: 0;
    width: 51px; height: 100%;
    background: var(--mauve);
  }

  .contact-list {
    position: absolute;
    left: 234px;
    top: 105px;
    list-style: none;
  }
  .contact-item {
    display: flex;
    align-items: center;
    gap: 6px;
    height: 24.5px;
    font-size: 16px;
    color: var(--ink);
  }
  .contact-item--web { color: var(--mauve); }
  .contact-item--social-first { margin-top: 14px; }
  .contact-item--social { height: 28px; }
  .contact-icon { width: 18px; height: 18px; flex: none; }

  .brand {
    position: absolute;
    left: 0; right: 0;
    top: 114px;
    text-align: center;
  }
  .brand-name {
    font-size: 32px;
    font-weight: 500;
    letter-spacing: 0.5px;
    color: var(--slate);
  }
  .tagline {
    margin-top: 32px;
    font-size: 20px;
    font-weight: 400;
    color: #e6e6e6;
  }
</style>
</head>
<body>
  <section class="card card--front">
    <div class="accent-band"></div>
    <ul class="contact-list">
      <li class="contact-item">
        <svg class="contact-icon" viewBox="0 0 18 18" aria-hidden="true">
          <rect x="1.5" y="1.5" width="15" height="15" rx="2" fill="none" stroke="var(--mauve)" stroke-width="1.4"/>
          <path d="M6 4.5c-.8.4-1.3 1.2-1 2.4.6 2.6 3.4 5.4 6 6 1.2.3 2-.2 2.4-1l-1.6-1.4-1.2.8c-1.2-.5-2.7-2-3.2-3.2l.8-1.2z" fill="var(--mauve)"/>
        </svg>
        <span>61 487 902 346</span>
      </li>
      <li class="contact-item">
        <svg class="contact-icon" viewBox="0 0 18 18" aria-hidden="true">
          <rect x="1.5" y="4" width="15" height="10" fill="var(--mauve)"/>
          <path d="M1.5 4.5 9 10l7.5-5.5" fill="none" stroke="var(--white)" stroke-width="1.2"/>
        </svg>
        <span>marisol@rwofficepartners.com.au</span>
      </li>
      <li class="contact-item contact-item--web">
        <svg class="contact-icon" viewBox="0 0 18 18" aria-hidden="true">
          <g fill="none" stroke="var(--mauve)" stroke-width="1.2">
            <circle cx="9" cy="9" r="7"/>
            <ellipse cx="9" cy="9" rx="3" ry="7"/>
            <path d="M2 9h14M3 5.5h12M3 12.5h12"/>
          </g>
        </svg>
        <span>www.rwofficepartners.com.au</span>
      </li>
      <li class="contact-item contact-item--social contact-item--social-first">
        <svg class="contact-icon" viewBox="0 0 18 18" aria-hidden="true">
          <circle cx="9" cy="9" r="8" fill="none" stroke="var(--slate)" stroke-width="1"/>
        </svg>
        <span>@rwofficepartners</span>
      </li>
      <li class="contact-item contact-item--social">
        <svg class="contact-icon" viewBox="0 0 18 18" aria-hidden="true">
          <circle cx="9" cy="9" r="8" fill="none" stroke="var(--slate)" stroke-width="1"/>
        </svg>
        <span>@rwofficepartners</span>
      </li>
    </ul>
  </section>

  <section class="card card--back">
    <div class="brand">
      <p class="brand-name">RW Office Partners</p>
      <p class="tagline">Your tidy answer finder</p>
    </div>
  </section>
</body>
</html>
```